" Perícias Solvane - Perícias e Administração Judicial é especializado em perícias, notadamente na execução de cálculos, pareceres e laudos, nas áreas contábil, tributária, financeira e cível, nas esferas judicial e extrajudicial. Presta serviços na condição de Perito do Juízo, e também como Perito Assistente, seja no embasamento técnico para a Petição Inicial, seja na fase de Conclusão Processual. Opera na Justiça de 1ª Instância nos Tribunais Estaduais, nos Tribunais da Justiça Federal e nos Tribunais Superiores. "

```html
<!DOCTYPE html>
<html lang="pt-BR">
<head>
<meta charset="utf-8">
<title>Pasta — Perícias Solvane</title>
<link href="https://fonts.googleapis.com/css2?family=Montserrat:wght@400;500;600&display=swap" rel="stylesheet">
<style>
  :root{
    --bg-light:#f4f4f5;
    --bg-mid:#e6e6e8;
    --folder:#333032;
    --folder-deep:#2b2829;
    --gold:#c9a867;
    --gold-dark:#8f7440;
    --gold-light:#e9d3a0;
    --text-light:#e8e6e3;
    --band:#2e2c2d;
  }
  html,body{margin:0;padding:0;overflow:hidden;}
  body{width:1200px;height:1200px;position:relative;
    background:linear-gradient(135deg,var(--bg-light) 0%,var(--bg-mid) 55%,var(--bg-light) 100%);
    font-family:"Montserrat",Arial,sans-serif;}
  .top-rule{position:absolute;left:0;top:24px;width:1200px;height:10px;
    background:linear-gradient(90deg,var(--gold-dark),var(--gold-light) 50%,var(--gold-dark));}
  .folder-art{position:absolute;left:0;top:0;}
  .services{position:absolute;left:132px;top:182px;margin:0;padding:0;list-style:none;
    color:var(--text-light);font-size:11.5px;font-weight:500;line-height:19px;}
  .services li::before{content:"";display:inline-block;width:6px;height:6px;border-radius:50%;
    background:var(--gold);margin-right:8px;vertical-align:1px;}
  .brand{position:absolute;color:var(--gold);font-weight:500;display:flex;align-items:center;gap:12px;}
  .brand .mark{width:18px;height:18px;background:var(--gold);flex:none;}
  .brand .name{display:block;letter-spacing:2px;line-height:1.02;}
  .brand .tagline{display:block;letter-spacing:.8px;margin-top:4px;white-space:nowrap;}
  .brand--front{left:712px;top:228px;}
  .brand--front .name{font-size:25px;}
  .brand--front .tagline{font-size:7px;}
  .brand--back{left:256px;top:452px;}
  .brand--back .name{font-size:22px;}
  .brand--back .tagline{font-size:6.5px;}
  .address{position:absolute;left:142px;top:752px;color:var(--text-light);font-size:11.5px;line-height:19px;margin:0;}
  .phones{position:absolute;left:478px;top:746px;margin:0;padding:0;list-style:none;color:var(--text-light);font-size:11.5px;line-height:26px;}
  .phones li{display:flex;align-items:center;gap:10px;}
  .phones svg{flex:none;}
  .label{position:absolute;left:0;width:1200px;top:1130px;text-align:center;color:#fff;
    font-size:22px;letter-spacing:14px;font-weight:400;}
</style>
</head>
<body>
  <div class="top-rule"></div>

  <svg class="folder-art" width="1200" height="1200" viewBox="0 0 1200 1200">
    <defs>
      <linearGradient id="goldBar" x1="0" x2="1">
        <stop offset="0" stop-color="#8f7440"/><stop offset=".5" stop-color="#e9d3a0"/><stop offset="1" stop-color="#8f7440"/>
      </linearGradient>
      <linearGradient id="goldTab" x1="0" x2="1">
        <stop offset="0" stop-color="#6f5a32"/><stop offset=".6" stop-color="#c9a867"/><stop offset="1" stop-color="#8f7440"/>
      </linearGradient>
    </defs>
    <rect x="108" y="156" width="984" height="660" fill="var(--folder)"/>
    <rect x="1064" y="156" width="6" height="660" fill="url(#goldBar)"/>
    <rect x="1080" y="156" width="6" height="660" fill="url(#goldBar)"/>
    <path d="M72 790 Q72 780 82 780 L108 780 L108 1005 L82 1005 Q72 1005 72 995 Z" fill="url(#goldTab)"/>
    <path d="M108 816 L1030 816 C960 870 720 830 520 880 C360 920 240 975 108 1005 Z" fill="var(--folder-deep)"/>
    <path d="M0 1092 C300 1062 900 1062 1200 1092 L1200 1200 L0 1200 Z" fill="var(--band)"/>
  </svg>

  <ul class="services">
    <li>Perícias Contábeis Judiciais e Extra Judiciais</li>
    <li>Avaliação Patrimonial e Empresarial</li>
    <li>Administração Judicial</li>
  </ul>

  <div class="brand brand--front">
    <span class="mark"></span>
    <span><span class="name">PERÍCIAS<br>SOLVANE</span><span class="tagline">PERÍCIAS E ADMINISTRAÇÃO JUDICIAL</span></span>
  </div>

  <div class="brand brand--back">
    <span class="mark"></span>
    <span><span class="name">PERÍCIAS<br>SOLVANE</span><span class="tagline">PERÍCIAS E ADMINISTRAÇÃO JUDICIAL</span></span>
  </div>

  <p class="address">Rua Alvorada Lima, 512 | Centro<br>Campo Claro/MS &nbsp;|&nbsp; CEP: 79000-120</p>

  <ul class="phones">
    <li>(67) 3000-4521
      <svg width="16" height="16" viewBox="0 0 16 16"><rect width="16" height="16" rx="2" fill="#c9a867"/><path d="M5 3.5l2 2.2-1 1.2c.6 1.3 1.6 2.3 2.9 2.9l1.2-1 2.2 2-1.2 1.7C7.8 12.3 3.7 8.2 3.5 4.7Z" fill="#333032"/></svg>
    </li>
    <li>(67) 9000-7184
      <svg width="16" height="16" viewBox="0 0 16 16"><rect width="16" height="16" rx="2" fill="#c9a867"/><rect x="5" y="3" width="6" height="10" rx="1" fill="#333032"/><rect x="6" y="4.5" width="4" height="6" fill="#c9a867"/></svg>
    </li>
  </ul>

  <div class="label">PASTA</div>
</body>
</html>
```